PSD website for property company

Please read the brief thoroughly.

We are looking for a new website for a property group that does property acquisitions, property development and property management.
They buy, build and lease core inner city industrial assets in Sydney, Australia.
They also invest in residential developments.

Site menu
- Home page
- Property – sub menus include – Leasing ; Projects ; Investments ; Property Management
- Capital and finance
- About
- Contact

They like this website
https://www.verlo.com.au/

They want the site to be clean, modern and bold.
They like few colors, even black and white is OK to submit

They have a logo and style guide and useable images here:
http://www.kumet.net/temp/PelorisWeb2019.zip
The zip file is also attached to this project.
We have supplied some images to give you an idea, but we will also require you to provide at least 3 extra images from stock photos.
Use your imagination.

I am expecting a lot of similar designs, so be aware the photos you choose will be really important.
They want really 3 good stock photos used and supplied without charge.
Please not too generic, I repeat the quality of the photos is important.
You may provide several photos (but not in multiple submissions please) and we will choose the best three to be provided.

The winner will be selected on a single home page design and required to provide;
All photos use in original format without charge
A second ‘standard page’ template design based on the winning home page design

```html
<!DOCTYPE html>
<html lang="en">
<head>
<meta charset="utf-8">
<title>Peloris — Property Development and Property Management</title>
<link rel="stylesheet" href="https://fonts.googleapis.com/css2?family=Oswald:wght@500;700&family=Roboto:wght@300;400;500&display=swap">
<style>
:root{
  --ink:#1f1f1f;
  --text:#555555;
  --sage:#8aa882;
  --olive:#546b2e;
  --mint:#f4f9ee;
  --footer:#2e2e2e;
  --footer-text:#cfcfcf;
  --white:#ffffff;
}
*{margin:0;padding:0;box-sizing:border-box}
html,body{width:1200px;height:3104px;overflow:hidden;background:var(--white)}
body{position:relative;font-family:'Roboto',sans-serif;color:var(--text)}
.abs{position:absolute}
.display{font-family:'Oswald',sans-serif;font-weight:700;color:var(--ink)}

/* hero */
.hero{left:0;top:0;width:1200px;height:628px;
  background:linear-gradient(180deg,#9fb6cc 0%,#c7d3dc 35%,#6f5a48 62%,#4a3a2e 85%,#3b3b33 100%)}
.brand{left:94px;top:24px;font-family:'Oswald',sans-serif;font-weight:500;font-size:40px;letter-spacing:9px;color:var(--white)}
.nav{left:0;top:46px;font-size:12.5px;font-weight:500;color:var(--white)}
.nav a{color:inherit;text-decoration:none;position:absolute;white-space:nowrap}
.phone{left:970px;top:41px;font-family:'Oswald',sans-serif;font-weight:500;font-size:15px;letter-spacing:.5px;color:var(--white);display:flex;align-items:center;gap:6px}
.hero-title{left:0;width:1200px;text-align:center;color:var(--white);font-family:'Oswald',sans-serif;font-weight:700}
.hero-title.small{top:234px;font-size:40px;line-height:1}
.hero-title.big{top:282px;font-size:68px;line-height:1}
.dot{left:97px;width:8px;height:8px;border-radius:50%;background:rgba(255,255,255,.6)}
.dot.on{background:var(--white);box-shadow:0 0 0 2px rgba(255,255,255,.4)}

/* welcome */
.photo-main{left:95px;top:554px;width:505px;height:556px;background:linear-gradient(180deg,#b7cde0 0%,#e8e6e0 45%,#8a8f76 80%,#6d6f62 100%)}
.photo-side{left:402px;top:921px;width:225px;height:291px;background:linear-gradient(180deg,#cfdbe4 0%,#6b4f3a 55%,#45382e 100%);border:2px solid var(--white)}
.welcome-title{left:650px;top:736px;font-size:46px;line-height:1.2}
.welcome-text{left:650px;top:806px;width:460px;font-size:13.9px;line-height:20.3px;font-weight:300;color:#444}
.btn{left:650px;top:945px;width:140px;height:41px;border-radius:21px;background:var(--sage);color:var(--white);
  font-family:'Oswald',sans-serif;font-weight:700;font-size:17px;display:flex;align-items:center;justify-content:center}

/* services */
.services-band{left:0;top:1242px;width:1200px;height:470px;background:linear-gradient(180deg,var(--mint) 0%,var(--mint) 60%,#ffffff 100%)}
.hex{width:229px;height:263px;top:1269px}
.hex svg.frame{position:absolute;left:0;top:0}
.hex .icon{position:absolute;left:50%;transform:translateX(-50%)}
.hex h3{position:absolute;left:0;width:229px;text-align:center;font-family:'Oswald',sans-serif;font-weight:700;font-size:22px;line-height:24px;color:var(--ink)}
.hex .rule{position:absolute;left:99px;width:31px;height:2px;background:var(--olive)}
.hex p{position:absolute;left:30px;width:169px;text-align:center;font-size:14px;line-height:20px;font-weight:300;color:#555}

/* capital */
.section-title{left:0;width:1200px;text-align:center;top:1638px;font-size:46px;line-height:1.2}
.card-photo{top:1716px;width:310px;height:240px}
.card-body{top:1926px;width:310px;height:174px;background:var(--mint);padding:20px 18px 0 18px}
.card-body h4{font-family:'Oswald',sans-serif;font-weight:700;font-size:21px;color:var(--ink);line-height:26px}
.card-body .rule{width:31px;height:2px;background:var(--olive);margin:4px 0 14px}
.card-body p{font-size:14px;line-height:19.5px;font-weight:300;color:#555}
.card-body .more{display:block;margin-top:11px;font-family:'Oswald',sans-serif;font-weight:700;font-size:14px;color:var(--sage)}

.tile{position:absolute}

/* footer */
.footer{left:0;top:2688px;width:1200px;height:416px;background:var(--footer)}
.f-brand{left:94px;top:2754px;font-family:'Oswald',sans-serif;font-weight:500;font-size:34px;letter-spacing:8px;color:var(--sage)}
.f-info{left:94px;font-size:12.5px;line-height:17px;color:var(--footer-text);display:flex;gap:10px;align-items:flex-start}
.f-head{top:2776px;font-family:'Oswald',sans-serif;font-weight:500;font-size:16px;color:var(--white)}
.f-list{top:2818px;list-style:none;font-size:12.5px;color:var(--footer-text)}
.f-list li{height:27px;line-height:16px}
.f-sub{left:789px;top:2810px;width:320px;font-size:12.5px;line-height:19px;color:var(--footer-text)}
.f-input{left:789px;top:2870px;width:318px;height:31px;border-bottom:1px solid #9a9a9a;font-size:11.5px;color:#8a8a8a;display:flex;align-items:center;justify-content:space-between}
.f-divider{left:0;top:3002px;width:1200px;height:1px;background:#4a4a4a}
.social{top:3025px;width:14px;height:14px;border-radius:50%;background:#8d8d8d}
.copy{left:0;width:1200px;top:3053px;text-align:center;font-size:12px;color:#a8a8a8}
.copy b{color:var(--white);font-weight:400}
</style>
</head>
<body>

<!-- hero -->
<div class="abs hero" role="img" aria-label="Street view of a brick mid-rise building with arched windows under a cloudy sky"></div>
<div class="abs brand">PELORIS</div>
<nav class="abs nav">
  <a style="left:426px">Home</a>
  <a style="left:503px">Property</a>
  <a style="left:601px">Capital and finance</a>
  <a style="left:758px">About</a>
  <a style="left:836px">Contact</a>
</nav>
<div class="abs phone">
  <svg width="14" height="14" viewBox="0 0 24 24"><path fill="#fff" d="M6.6 10.8a15.1 15.1 0 0 0 6.6 6.6l2.2-2.2c.3-.3.7-.4 1-.2 1.1.4 2.3.6 3.6.6.6 0 1 .4 1 1V20c0 .6-.4 1-1 1A17 17 0 0 1 3 4c0-.6.4-1 1-1h3.5c.6 0 1 .4 1 1 0 1.3.2 2.5.6 3.6.1.3 0 .7-.2 1z"/></svg>
  02-555-014-273
</div>
<div class="abs hero-title small">Property Development and</div>
<div class="abs hero-title big">Property Management</div>
<div class="abs dot on" style="top:291px"></div>
<div class="abs dot" style="top:312px"></div>
<div class="abs dot" style="top:330px"></div>

<!-- welcome -->
<div class="abs photo-main" role="img" aria-label="Pale stone building with arched ground floor and landscaped grass"></div>
<div class="abs photo-side" role="img" aria-label="Brick building facade with arched windows and a tree"></div>
<h1 class="abs display welcome-title">Welcome to Peloris</h1>
<p class="abs welcome-text">Lorem ipsum dolor sit amet, consectetur adipiscing elit. Fusce eu sodales velit, vitae iaculis ex. Maecenas vitae ligula vel odio malesuada accumsan ac eget nisl. Aenean tempus velit at ante lobortis, eleifend mollis sapien gravida.&nbsp; Sed vitae urna est. Donec fringilla felis in nisi aliquet eleifend. Maecenas nec luctus lectus. Morbi sed quam vestibulum, lobortis magna in, porttitor ex.</p>
<div class="abs btn">Read More</div>

<!-- services -->
<div class="abs services-band"></div>

<div class="abs hex" style="left:94px">
  <svg class="frame" width="229" height="263" viewBox="0 0 229 263"><polygon points="114.5,8 222,70 222,193 114.5,255 7,193 7,70" fill="none" stroke="#546b2e" stroke-width="12"/></svg>
  <svg class="icon" style="top:56px" width="66" height="62" viewBox="0 0 66 62" fill="none" stroke="#546b2e" stroke-width="2.2">
    <path d="M4 2h34l8 8v30"/><path d="M4 2v56h24"/><path d="M11 14h22M11 21h26M11 28h18"/>
    <path d="M30 44l16-14 16 14"/><path d="M34 41v17h24V41"/><path d="M42 58v-9h8v9"/>
  </svg>
  <h3 style="top:134px">Leasing</h3>
  <div class="rule" style="top:162px"></div>
  <p style="top:170px">Lorem ipsum dor sit amet, cosecur adipisc</p>
</div>

<div class="abs hex" style="left:355px">
  <svg class="frame" width="229" height="263" viewBox="0 0 229 263"><polygon points="114.5,8 222,70 222,193 114.5,255 7,193 7,70" fill="none" stroke="#546b2e" stroke-width="12"/></svg>
  <svg class="icon" style="top:58px" width="62" height="60" viewBox="0 0 62 60" fill="none" stroke="#546b2e" stroke-width="2.2">
    <path d="M4 58V12h54v46"/><path d="M20 12V3h22v9"/><path d="M1 58h60"/>
    <rect x="10" y="19" width="9" height="8"/><rect x="26" y="19" width="9" height="8"/><rect x="42" y="19" width="9" height="8"/>
    <rect x="10" y="33" width="9" height="8"/><rect x="26" y="33" width="9" height="8"/><rect x="42" y="33" width="9" height="8"/>
    <path d="M26 58V47h10v11"/>
  </svg>
  <h3 style="top:134px">Projects</h3>
  <div class="rule" style="top:162px"></div>
  <p style="top:170px">Lorem ipsum dor sit amet, cosecur adipisc</p>
</div>

<div class="abs hex" style="left:616px">
  <svg class="frame" width="229" height="263" viewBox="0 0 229 263"><polygon points="114.5,8 222,70 222,193 114.5,255 7,193 7,70" fill="none" stroke="#546b2e" stroke-width="12"/></svg>
  <svg class="icon" style="top:78px" width="68" height="40" viewBox="0 0 68 40" fill="#546b2e">
    <rect x="2" y="32" width="12" height="6" rx="3"/>
    <rect x="17" y="26" width="12" height="5" rx="2.5"/><rect x="17" y="32" width="12" height="6" rx="3"/>
    <rect x="32" y="20" width="12" height="5" rx="2.5"/><rect x="32" y="26" width="12" height="5" rx="2.5"/><rect x="32" y="32" width="12" height="6" rx="3"/>
    <rect x="47" y="8" width="14" height="5" rx="2.5"/><rect x="47" y="14" width="14" height="5" rx="2.5"/><rect x="47" y="20" width="14" height="5" rx="2.5"/><rect x="47" y="26" width="14" height="5" rx="2.5"/><rect x="47" y="32" width="14" height="6" rx="3"/>
  </svg>
  <h3 style="top:134px">Investments</h3>
  <div class="rule" style="top:162px"></div>
  <p style="top:170px">Lorem ipsum dor sit amet, cosecur adipisc</p>
</div>

<div class="abs hex" style="left:877px">
  <svg class="frame" width="229" height="263" viewBox="0 0 229 263"><polygon points="114.5,8 222,70 222,193 114.5,255 7,193 7,70" fill="none" stroke="#546b2e" stroke-width="12"/></svg>
  <svg class="icon" style="top:52px" width="60" height="56" viewBox="0 0 60 56" fill="none" stroke="#546b2e" stroke-width="2.2">
    <path d="M4 30l14-14 10 10"/><path d="M20 4l12 12-8 8"/><circle cx="34" cy="12" r="7"/>
    <rect x="28" y="30" width="24" height="10"/><path d="M24 40h32v6H24z"/><path d="M22 50h36"/>
  </svg>
  <h3 style="top:112px">Property<br>Management</h3>
  <div class="rule" style="top:162px"></div>
  <p style="top:170px">Lorem ipsum dor sit amet, cosecur adipisc</p>
</div>

<!-- capital and finance -->
<h2 class="abs display section-title">Capital and Finance</h2>

<div class="abs card-photo" style="left:94px;background:linear-gradient(135deg,#c79a3b 0%,#6d5d3a 40%,#e6ecf2 60%,#3d5c85 100%)" role="img" aria-label="Glass skyscrapers seen from below in golden sunlight"></div>
<div class="abs card-body" style="left:76px">
  <h4>Nullam consectetur</h4><div class="rule"></div>
  <p>Suspendisse in est vel nisi placerat dictum ut non purus. Vivamus pretium dapibus velit ut lacinia.</p>
  <span class="more">Read More</span>
</div>

<div class="abs card-photo" style="left:446px;background:linear-gradient(160deg,#5f86a8 0%,#3b4f5e 45%,#8aa36a 75%,#b8b8b4 100%)" role="img" aria-label="Office tower walkway lined with trees"></div>
<div class="abs card-body" style="left:428px">
  <h4>Etiam rhoncus</h4><div class="rule"></div>
  <p>Suspendisse in est vel nisi placerat dictum ut non purus. Vivamus pretium dapibus velit ut lacinia.</p>
  <span class="more">Read More</span>
</div>

<div class="abs card-photo" style="left:797px;background:linear-gradient(180deg,#a9c4e6 0%,#4e6d92 45%,#5a7a4c 75%,#9a9a98 100%)" role="img" aria-label="City towers beyond a paved plaza with hedges"></div>
<div class="abs card-body" style="left:779px">
  <h4>Nam ultricies</h4><div class="rule"></div>
  <p>Suspendisse in est vel nisi placerat dictum ut non purus. Vivamus pretium dapibus velit ut lacinia.</p>
  <span class="more">Read More</span>
</div>

<!-- gallery -->
<div class="tile" style="left:94px;top:2123px;width:253px;height:253px;background:linear-gradient(180deg,#5d9bd6 0%,#a7bfd3 45%,#4f7a46 80%,#bdbdb8 100%)" role="img" aria-label="Office buildings behind a park"></div>
<div class="tile" style="left:347px;top:2123px;width:253px;height:253px;background:linear-gradient(150deg,#2f5b8d 0%,#9dc2e6 50%,#2a4f78 100%)" role="img" aria-label="Skyscrapers against blue sky from below"></div>
<div class="tile" style="left:600px;top:2123px;width:506px;height:253px;background:linear-gradient(160deg,#eef1f3 0%,#d6dbe0 40%,#7d8691 75%,#e4e7ea 100%)" role="img" aria-label="Angular glass building corner against pale sky"></div>
<div class="tile" style="left:94px;top:2376px;width:506px;height:253px;background:linear-gradient(100deg,#3c6e25 0%,#8fb8df 35%,#dfeaf5 55%,#3f6ea3 100%)" role="img" aria-label="Trees and glass towers seen upward toward the sun"></div>
<div class="tile" style="left:600px;top:2376px;width:253px;height:253px;background:linear-gradient(180deg,#7aaee0 0%,#6d86a6 50%,#4c7a3c 90%)" role="img" aria-label="Tall residential blocks above green trees"></div>
<div class="tile" style="left:853px;top:2376px;width:253px;height:253px;background:linear-gradient(160deg,#f0d7b5 0%,#b78a7a 45%,#6b5d73 75%,#8d6b5c 100%)" role="img" aria-label="Boardwalk beside glass facade at sunset"></div>

<!-- footer -->
<footer class="abs footer"></footer>
<div class="abs f-brand">PELORIS</div>

<div class="abs f-info" style="top:2823px">
  <svg width="12" height="16" viewBox="0 0 12 16"><path fill="#b5b5b5" d="M6 0a6 6 0 0 0-6 6c0 4.5 6 10 6 10s6-5.5 6-10a6 6 0 0 0-6-6zm0 8.3A2.3 2.3 0 1 1 6 3.7a2.3 2.3 0 0 1 0 4.6z"/></svg>
  <span>18 Harbour Lane, Suite 200<br>Harold Penwick</span>
</div>
<div class="abs f-info" style="top:2864px">
  <svg width="14" height="11" viewBox="0 0 14 11"><rect x=".5" y=".5" width="13" height="10" fill="none" stroke="#b5b5b5"/><path d="M.5.5l6.5 5.5 6.5-5.5" fill="none" stroke="#b5b5b5"/></svg>
  <span>info@peloris.com</span>
</div>
<div class="abs f-info" style="top:2891px">
  <svg width="14" height="14" viewBox="0 0 24 24"><path fill="#b5b5b5" d="M6.6 10.8a15.1 15.1 0 0 0 6.6 6.6l2.2-2.2c.3-.3.7-.4 1-.2 1.1.4 2.3.6 3.6.6.6 0 1 .4 1 1V20c0 .6-.4 1-1 1A17 17 0 0 1 3 4c0-.6.4-1 1-1h3.5c.6 0 1 .4 1 1 0 1.3.2 2.5.6 3.6.1.3 0 .7-.2 1z"/></svg>
  <span>02-555-014-273</span>
</div>

<div class="abs f-head" style="left:401px">Sitemap</div>
<ul class="abs f-list" style="left:402px">
  <li>Home</li><li>Property</li><li>Capital and finance</li><li>About</li><li>Contact</li>
</ul>

<div class="abs f-head" style="left:617px">Actions</div>
<ul class="abs f-list" style="left:617px">
  <li>Leasing</li><li>Projects</li><li>Investments</li><li>Property<br>Management</li>
</ul>

<div class="abs f-head" style="left:789px">Subscribe Newsletter</div>
<p class="abs f-sub">Subscribe to our newsletter and always be aware of all the information</p>
<div class="abs f-input">
  <span>Enter your email address</span>
  <svg width="15" height="11" viewBox="0 0 15 11"><rect width="15" height="11" fill="#e6e6e6"/><path d="M0 0l7.5 6L15 0" fill="none" stroke="#2e2e2e" stroke-width="1.2"/></svg>
</div>

<div class="abs f-divider"></div>
<div class="abs social" style="left:563px"></div>
<div class="abs social" style="left:591px"></div>
<div class="abs social" style="left:619px"></div>
<div class="abs copy">© 2019 <b>Peloris</b>. All Right Reserved.</div>

</body>
</html>
```